Gummy Label design for hemp company

I need a 3.25 inch wide by 4 inch tall label made to be put on bags of gummies. I will include all disclaimers that need to be there, as well as my logo. This is for our 25 mg Delta 8 gummies 20ct, but I will use the design for our entire gummy line, just editing the text. Needs to have ingredient list. Ingredients: Sugar, Inulin, Corn syrup, water, pectin, citric acid, baking soda, fruit, hemp extract.

Everything should be on one label as this is going on a sticker that will be placed on a bag.
I would like to highlight that they are vegan if possible.

• Must have the following disclaimer: "Contains Farm Bill compliant hemp extract. These statements have not been evaluated by the KWT. This product is NOT intended to treat, cure, or prevent any disease. Do not operate heavy machinery while using this product. This product may cause you to fail a drug test. Consult with your doctor before trying any new products. Do not take if pregnant or lactating. If you experience any adverse effects, discontinue use and seek advice from your physician."
• NEEDS TO SAY: "100% hemp derived" also "<.3% D9 THC"

```html
<!DOCTYPE html>
<html lang="en">
<head>
<meta charset="utf-8">
<title>SunnyLeaf Hemp – Delta 8 Gummy Labels</title>
<link href="https://fonts.googleapis.com/css2?family=Montserrat:wght@400;500;700;800;900&display=swap" rel="stylesheet">
<style>
  :root {
    --page: #ffffff;
    --brand-green: #2e7d32;
    --lime: #8cc63f;
    --dark-green-text: #1e5a23;
    --ink: #1a1a1a;
    --gold-light: #f0c23a;
    --gold-dark: #9a6a22;
    --purple-a: #3c2e91;
    --purple-b: #c81d8d;
    --violet-a: #5a2a8c;
    --violet-b: #6e2d94;
    --violet-text: #5b2a8e;
    --forest: #1f3a1c;
    --forest-text: #1d3a1c;
    --navy: #1d3d7f;
  }
  * { box-sizing: border-box; margin: 0; padding: 0; }
  html, body {
    width: 1050px; height: 1200px; overflow: hidden;
    background: var(--page);
    font-family: "Montserrat", sans-serif;
  }
  .sheet { position: relative; width: 1050px; height: 1200px; }

  .label {
    position: absolute;
    width: 391px; height: 481px;
    background: var(--frame);
  }
  .label--sunset { left: 113px; top: 75px;  --frame: linear-gradient(90deg, var(--purple-a), var(--purple-b)); }
  .label--violet { left: 535px; top: 75px;  --frame: linear-gradient(90deg, var(--violet-a), var(--violet-b)); }
  .label--forest { left: 99px;  top: 614px; --frame: var(--forest); }
  .label--navy   { left: 521px; top: 614px; --frame: var(--navy); }

  .front-panel {
    position: absolute; left: 27px; top: 27px;
    width: 337px; height: 322px;
    background: #fff;
  }
  .vegan-mark {
    position: absolute; right: 18px; top: 11px;
    width: 45px; height: 45px;
    border: 3px solid var(--brand-green);
    border-radius: 5px;
  }
  .brand {
    position: absolute; left: 0; right: 0; top: 22px;
    display: flex; flex-direction: column; align-items: center; gap: 10px;
  }
  .brand-square {
    width: 52px; height: 52px;
    border: 4px solid var(--brand-green);
  }
  .brand-name {
    font-weight: 800; font-size: 29px; letter-spacing: -0.5px;
    color: var(--brand-green); line-height: 1;
  }
  .strength {
    position: absolute; left: 0; right: 0; top: 171px;
    text-align: center; font-weight: 800; font-size: 28px;
    line-height: 1; letter-spacing: 0.2px;
  }
  .product {
    position: absolute; left: 0; right: 0; top: 200px;
    text-align: center; font-weight: 900; font-size: 47px;
    line-height: 1; letter-spacing: 0.5px;
  }
  .headline-gold {
    background: linear-gradient(90deg, var(--gold-light), var(--gold-dark) 35%, var(--gold-light) 60%, var(--gold-dark) 85%, var(--gold-light));
    -webkit-background-clip: text; background-clip: text; color: transparent;
  }
  .headline-violet { color: var(--violet-text); }
  .headline-forest { color: var(--forest-text); }

  .divider {
    position: absolute; left: 143px; top: 248px;
    width: 51px; height: 3px;
    background: linear-gradient(90deg, var(--brand-green) 50%, var(--lime) 50%);
  }
  .claim {
    position: absolute; left: 0; right: 0;
    text-align: center; font-weight: 800; font-size: 17px; line-height: 1;
  }
  .claim--hemp { top: 260px; color: var(--lime); }
  .claim--thc  { top: 282px; color: var(--dark-green-text); }

  .count-badge {
    position: absolute; left: 15px; top: 269px;
    width: 45px; height: 45px; border-radius: 50%;
    border: 1.5px solid var(--brand-green);
    display: flex; flex-direction: column; align-items: center; justify-content: center;
    color: var(--brand-green); line-height: 0.9;
  }
  .count-number { font-weight: 700; font-size: 20px; }
  .count-word { font-weight: 500; font-size: 7px; letter-spacing: 0.3px; }

  .info-panel {
    position: absolute; left: 28px; top: 361px;
    width: 334px; height: 100px;
    background: #fff; border-radius: 3px;
    padding: 8px 12px 0 13px;
    color: var(--ink);
  }
  .ingredients { font-size: 9.3px; font-weight: 500; line-height: 1.45; }
  .ingredients strong { color: var(--brand-green); font-weight: 800; }
  .disclaimer { font-size: 7.2px; line-height: 1.3; margin-top: 2px; margin-left: -2px; }
</style>
</head>
<body>
<main class="sheet">

  <section class="label label--sunset" role="img" aria-label="Gummy label with gold hemp-leaf outline pattern on a purple to magenta border">
    <div class="front-panel">
      <div class="vegan-mark"></div>
      <div class="brand"><div class="brand-square"></div><div class="brand-name">SunnyLeaf Hemp</div></div>
      <div class="strength headline-gold">25 MG DELTA 8</div>
      <div class="product headline-gold">GUMMIES</div>
      <div class="divider"></div>
      <div class="claim claim--hemp">100% HEMP DERIVED</div>
      <div class="claim claim--thc">&lt;.3% D9 THC</div>
      <div class="count-badge"><span class="count-number">20</span><span class="count-word">COUNT</span></div>
    </div>
    <div class="info-panel">
      <p class="ingredients"><strong>INGREDIENTS:</strong> Sugar, Inulin, Corn Syrup, Water, Pectin, Citric Acid, Baking Soda, Fruit, Hemp Extract.</p>
      <p class="disclaimer">Contains Farm Bill compliant hemp extract. These statements have not been evaluated by the KWT. This product is NOT intended to treat, cure, or prevent any disease. Do not operate heavy machinery while using this product. This product may cause you to fail a drug test. Consult with your doctor before trying any new products. Do not take if pregnant or lactating. If you experience any adverse effects, discontinue use and seek advice from your physician.</p>
    </div>
  </section>

  <section class="label label--violet" role="img" aria-label="Gummy label with gold hemp-leaf outline pattern on a purple border">
    <div class="front-panel">
      <div class="vegan-mark"></div>
      <div class="brand"><div class="brand-square"></div><div class="brand-name">SunnyLeaf Hemp</div></div>
      <div class="strength headline-violet">25 MG DELTA 8</div>
      <div class="product headline-violet">GUMMIES</div>
      <div class="divider"></div>
      <div class="claim claim--hemp">100% HEMP DERIVED</div>
      <div class="claim claim--thc">&lt;.3% D9 THC</div>
      <div class="count-badge"><span class="count-number">20</span><span class="count-word">COUNT</span></div>
    </div>
    <div class="info-panel">
      <p class="ingredients"><strong>INGREDIENTS:</strong> Sugar, Inulin, Corn Syrup, Water, Pectin, Citric Acid, Baking Soda, Fruit, Hemp Extract.</p>
      <p class="disclaimer">Contains Farm Bill compliant hemp extract. These statements have not been evaluated by the KWT. This product is NOT intended to treat, cure, or prevent any disease. Do not operate heavy machinery while using this product. This product may cause you to fail a drug test. Consult with your doctor before trying any new products. Do not take if pregnant or lactating. If you experience any adverse effects, discontinue use and seek advice from your physician.</p>
    </div>
  </section>

  <section class="label label--forest" role="img" aria-label="Gummy label with gold hemp-leaf outline pattern on a dark green border">
    <div class="front-panel">
      <div class="vegan-mark"></div>
      <div class="brand"><div class="brand-square"></div><div class="brand-name">SunnyLeaf Hemp</div></div>
      <div class="strength headline-forest">25 MG DELTA 8</div>
      <div class="product headline-forest">GUMMIES</div>
      <div class="divider"></div>
      <div class="claim claim--hemp">100% HEMP DERIVED</div>
      <div class="claim claim--thc">&lt;.3% D9 THC</div>
      <div class="count-badge"><span class="count-number">20</span><span class="count-word">COUNT</span></div>
    </div>
    <div class="info-panel">
      <p class="ingredients"><strong>INGREDIENTS:</strong> Sugar, Inulin, Corn Syrup, Water, Pectin, Citric Acid, Baking Soda, Fruit, Hemp Extract.</p>
      <p class="disclaimer">Contains Farm Bill compliant hemp extract. These statements have not been evaluated by the KWT. This product is NOT intended to treat, cure, or prevent any disease. Do not operate heavy machinery while using this product. This product may cause you to fail a drug test. Consult with your doctor before trying any new products. Do not take if pregnant or lactating. If you experience any adverse effects, discontinue use and seek advice from your physician.</p>
    </div>
  </section>

  <section class="label label--navy" role="img" aria-label="Gummy label with gold hemp-leaf outline pattern on a navy blue border">
    <div class="front-panel">
      <div class="vegan-mark"></div>
      <div class="brand"><div class="brand-square"></div><div class="brand-name">SunnyLeaf Hemp</div></div>
      <div class="strength headline-gold">25 MG DELTA 8</div>
      <div class="product headline-gold">GUMMIES</div>
      <div class="divider"></div>
      <div class="claim claim--hemp">100% HEMP DERIVED</div>
      <div class="claim claim--thc">&lt;.3% D9 THC</div>
      <div class="count-badge"><span class="count-number">20</span><span class="count-word">COUNT</span></div>
    </div>
    <div class="info-panel">
      <p class="ingredients"><strong>INGREDIENTS:</strong> Sugar, Inulin, Corn Syrup, Water, Pectin, Citric Acid, Baking Soda, Fruit, Hemp Extract.</p>
      <p class="disclaimer">Contains Farm Bill compliant hemp extract. These statements have not been evaluated by the KWT. This product is NOT intended to treat, cure, or prevent any disease. Do not operate heavy machinery while using this product. This product may cause you to fail a drug test. Consult with your doctor before trying any new products. Do not take if pregnant or lactating. If you experience any adverse effects, discontinue use and seek advice from your physician.</p>
    </div>
  </section>

</main>
</body>
</html>
```